Vel Moro A4 paper and card metallic new packaging

Vel Moro New Packaging Brief
We need a CLASSIC packaging design which wraps around the bottom left side of the product (A4 card) in the shape of a square (front & back) for an existing brand name call Vel Moro. This is then covered in a polybag. This needs to display the most important detail about the product on the FRONT and then the other information on the back.
See images attached of some ideas
The packaging needs to be CLEAN and simple to portray the fact the product is of a Premium Luxurious quality.
It is sold in a store where it sits on a shelf so we need the following information portrayed very clearly so the consumer can see it straight away and know what the product is:
The below points need to be shown on the FRONT of the packaging - Information is listed in order of importance.
1.Premium Luxurious Card
2. Metallic
3. A4
4.The Colour (eg, Silver)
5.25 Pack
6. Logo – this can be small

These need to be shown on the BACK of the packaging - Information is listed in order of importance.
1.PREMIUM Luxurious Card
2.
• Ideal for card making for all occasions
• Invitations for all Celebrations
• Creative card & paper for presentations
3. Acid free
4. Made in china
5. Logo – this can be small
6.Barcode

Background
Vel Moro is a brand which sells PREMIUM Luxurious Paper and card stock which can be used for card making, invites, presentations. The colour range is approx. 24 colours and it comes in metallic and weave. It includes the following
*A4 Card 260gsm & paper 120gsm
*DL & C6 envelopes 120gsm

PLEASE READ ALL UPLOADED FILE NAMES.

Target Market(s)

Office supply and invitation market

Industry/Entity Type

Store

Requirements
Must have
• Most important is to have a style of packaging that suits and displays the product. Needs to be fresh and clean packaging but also show quality and show the actual product.
• Font should be simple, easy to read, clear so consumers can read what the product is straight away.
• Colours – can match the logo but we are open to other ideas as well.
• The colour range of the card we sell is 24 different colours so the actual packaging needs to match all colours and stand out.

```html
<!DOCTYPE html>
<html lang="en">
<head>
<meta charset="utf-8">
<title>Vel Moro Premium Metallic Card – Packaging</title>
<link rel="stylesheet" href="https://fonts.googleapis.com/css2?family=Arimo:wght@400;700&display=swap">
<style>
  :root {
    --ink: #111111;
    --ink-soft: #2a2a2a;
    --band: #0b0b0b;
    --gold: #c9a24b;
    --gold-light: #e6c77a;
    --brand: #4fb0c9;
    --link: #1c8fd6;
    --paper: #ffffff;
    --tab: #cfcfcf;
    --metal-hi: #c4c0bf;
    --metal-mid: #948c8b;
    --metal-lo: #5a5050;
  }
  html, body {
    margin: 0;
    width: 1200px;
    height: 1000px;
    overflow: hidden;
    background: var(--paper);
    font-family: "Arimo", Arial, sans-serif;
    color: var(--ink);
  }
  .canvas { position: relative; width: 1200px; height: 1000px; }

  /* metallic card sheets */
  .sheet {
    position: absolute;
    background:
      radial-gradient(ellipse 70% 45% at 25% 35%, rgba(235,235,232,.55), rgba(235,235,232,0) 70%),
      linear-gradient(172deg, var(--metal-hi) 0%, #aaa4a3 30%, var(--metal-mid) 60%, var(--metal-lo) 100%);
    box-shadow: 3px 4px 7px rgba(0,0,0,.35);
    overflow: hidden;
  }
  .sheet--a4-light  { left: 70px;  top: 70px;  width: 322px; height: 430px; }
  .sheet--a4-heavy  { left: 405px; top: 70px;  width: 322px; height: 430px; }
  .sheet--dl        { left: 750px; top: 162px; width: 168px; height: 338px; }
  .sheet--c6        { left: 940px; top: 252px; width: 175px; height: 248px; }
  .sheet--a4-light-back { left: 70px;  top: 515px; width: 322px; height: 428px; }
  .sheet--a4-heavy-back { left: 405px; top: 515px; width: 322px; height: 428px; }
  .sheet--dl-back   { left: 750px; top: 515px; width: 168px; height: 337px; }
  .sheet--c6-back   { left: 940px; top: 515px; width: 175px; height: 250px; }

  /* front wrap label */
  .front-label {
    position: absolute;
    left: 0;
    bottom: 3px;
    box-shadow: 2px 2px 4px rgba(0,0,0,.3);
    display: block;
  }
  .front-label--a4 { width: 142px; height: 142px; }
  .front-label--env { width: 112px; height: 122px; }
  .front-label text { font-family: "Arimo", Arial, sans-serif; }

  /* back wrap label */
  .back-label {
    position: absolute;
    left: 0; top: 0; bottom: 0;
    width: 14.4em;
    font-size: var(--u, 10px);
    background: var(--paper);
    box-shadow: 2px 0 4px rgba(0,0,0,.3);
    display: flex;
    flex-direction: column;
    overflow: hidden;
    --cols: 3;
  }
  .back-label--dl { --u: 8px; }
  .back-label--c6 { --u: 8.1px; --cols: 4; }

  .back-label__top { position: relative; height: 6.5em; flex: none; }
  .back-label__top svg,
  .back-label__bottom svg { position: absolute; inset: 0; width: 100%; height: 100%; }

  .brand {
    position: absolute;
    left: 1.2em; top: 1.3em;
    display: flex; align-items: center; gap: .35em;
    color: var(--brand);
    font-size: 1.15em;
    font-weight: 400;
    white-space: nowrap;
  }
  .brand__dot { width: .55em; height: .55em; border-radius: 50%; background: var(--brand); }

  .back-label__title { text-align: right; padding-right: .4em; margin-top: -1.3em; line-height: 1.05; flex: none; }
  .back-label__title .product { display: block; font-size: 1.45em; color: var(--ink); }
  .back-label__title .finish { display: block; font-size: .95em; color: var(--ink-soft); }

  .uses {
    margin: 1.4em 0 0 1em; padding: 0;
    list-style: none;
    font-size: .5em; line-height: 1.45;
    flex: none;
  }
  .uses li::before { content: "•"; margin-right: .6em; }

  .gallery {
    display: grid;
    grid-template-columns: repeat(var(--cols), 1fr);
    gap: .25em;
    padding: 0 .9em;
    margin-top: 1em;
    flex: none;
  }
  .gallery__tile { aspect-ratio: 1; border-radius: .3em; border: .12em solid #bbb; }

  .more-info { font-size: .48em; line-height: 1.3; margin: 1.6em 1.4em 0 2em; flex: none; }
  .more-info a { color: var(--link); text-decoration: none; font-weight: 700; }
  .range { font-size: .48em; line-height: 1.3; margin: 1.6em 1em 0 2em; flex: none; }
  .range ul { list-style: none; margin: .3em 0 0; padding: 0; }
  .range li::before { content: "•"; margin-right: .6em; }

  .back-label__bottom { position: absolute; left: 0; right: 0; bottom: 0; height: 6em; }
  .origin {
    position: absolute; right: 1.6em; bottom: 2.6em;
    color: var(--paper); font-size: .45em; font-weight: 700;
  }

  /* compact C6 back: keeps all text clear of the bottom band */
  .back-label--c6 .back-label__top { height: 5.2em; }
  .back-label--c6 .brand { top: 1em; }
  .back-label--c6 .back-label__title { margin-top: -1em; }
  .back-label--c6 .uses { margin-top: .9em; line-height: 1.3; }
  .back-label--c6 .gallery { margin-top: .6em; padding: 0 1.2em; }
  .back-label--c6 .more-info { margin-top: 1.2em; line-height: 1.15; }
  .back-label--c6 .range { margin-top: 1.2em; line-height: 1.15; }
  .back-label--c6 .back-label__bottom { height: 3.6em; }
  .back-label--c6 .origin { bottom: 1.4em; }
</style>
</head>
<body>
<main class="canvas">

  <!-- FRONT: A4 120gsm -->
  <section class="sheet sheet--a4-light" aria-label="A4 metallic card, front">
    <svg class="front-label front-label--a4" viewBox="0 0 142 142">
      <rect width="142" height="142" fill="var(--paper)"/>
      <path d="M0 0H142V11C95 13 40 20 0 30Z" fill="var(--band)"/>
      <path d="M0 31C40 21 95 14 142 12" fill="none" stroke="var(--gold)" stroke-width="2"/>
      <circle cx="9" cy="12" r="3" fill="var(--brand)"/>
      <text x="15" y="15" font-size="9" fill="var(--brand)">Vel Moro</text>
      <text x="140" y="40" font-size="16.5" text-anchor="end" fill="var(--ink)">Premium</text>
      <text x="140" y="51" font-size="10.5" text-anchor="end" fill="var(--ink-soft)">Metallic Card</text>
      <circle cx="25" cy="82" r="10" fill="none" stroke="var(--ink)" stroke-width="1.5"/>
      <text x="72" y="104" font-size="46" fill="var(--ink)">A4</text>
      <rect x="14" y="114" width="54" height="22" fill="var(--tab)" stroke="#555" stroke-width=".6"/>
      <text x="41" y="129" font-size="11" font-weight="700" text-anchor="middle" fill="var(--ink)">Silver</text>
      <rect x="71" y="115" width="62" height="20" fill="none" stroke="#333" stroke-width=".6"/>
      <line x1="71" y1="125" x2="133" y2="125" stroke="#333" stroke-width=".6"/>
      <text x="102" y="123" font-size="7.5" text-anchor="middle" fill="var(--ink)">25 Pack</text>
      <text x="102" y="133" font-size="6" text-anchor="middle" fill="var(--ink)">120gsm</text>
    </svg>
  </section>

  <!-- FRONT: A4 260gsm -->
  <section class="sheet sheet--a4-heavy" aria-label="A4 metallic card 260gsm, front">
    <svg class="front-label front-label--a4" viewBox="0 0 142 142">
      <rect width="142" height="142" fill="var(--paper)"/>
      <path d="M0 0H142V11C95 13 40 20 0 30Z" fill="var(--band)"/>
      <path d="M0 31C40 21 95 14 142 12" fill="none" stroke="var(--gold)" stroke-width="2"/>
      <circle cx="9" cy="12" r="3" fill="var(--brand)"/>
      <text x="15" y="15" font-size="9" fill="var(--brand)">Vel Moro</text>
      <text x="140" y="40" font-size="16.5" text-anchor="end" fill="var(--ink)">Premium</text>
      <text x="140" y="51" font-size="10.5" text-anchor="end" fill="var(--ink-soft)">Metallic Card</text>
      <circle cx="25" cy="82" r="10" fill="none" stroke="var(--ink)" stroke-width="1.5"/>
      <text x="72" y="104" font-size="46" fill="var(--ink)">A4</text>
      <rect x="14" y="114" width="54" height="22" fill="var(--tab)" stroke="#555" stroke-width=".6"/>
      <text x="41" y="129" font-size="11" font-weight="700" text-anchor="middle" fill="var(--ink)">Silver</text>
      <rect x="71" y="115" width="62" height="20" fill="none" stroke="#333" stroke-width=".6"/>
      <line x1="71" y1="125" x2="133" y2="125" stroke="#333" stroke-width=".6"/>
      <text x="102" y="123" font-size="7.5" text-anchor="middle" fill="var(--ink)">25 Pack</text>
      <text x="102" y="133" font-size="6" text-anchor="middle" fill="var(--ink)">260gsm</text>
    </svg>
  </section>

  <!-- FRONT: DL envelopes -->
  <section class="sheet sheet--dl" aria-label="DL metallic envelopes, front">
    <svg class="front-label front-label--env" viewBox="0 0 112 122">
      <rect width="112" height="122" fill="var(--paper)"/>
      <path d="M0 0H112V9C75 11 30 16 0 24Z" fill="var(--band)"/>
      <path d="M0 25C30 17 75 11 112 10" fill="none" stroke="var(--gold)" stroke-width="1.7"/>
      <circle cx="6" cy="10" r="2.5" fill="var(--brand)"/>
      <text x="11" y="13" font-size="7.5" fill="var(--brand)">Vel Moro</text>
      <text x="109" y="38" font-size="13" text-anchor="end" fill="var(--ink)">Premium</text>
      <text x="109" y="48" font-size="9" text-anchor="end" fill="var(--ink-soft)">Metallic Card</text>
      <circle cx="21" cy="72" r="8" fill="none" stroke="var(--ink)" stroke-width="1.3"/>
      <text x="75" y="88" font-size="30" text-anchor="middle" fill="var(--ink)">DL</text>
      <text x="75" y="96" font-size="6" text-anchor="middle" fill="var(--ink)">ENVELOPES</text>
      <rect x="10" y="102" width="46" height="17" fill="var(--tab)" stroke="#555" stroke-width=".5"/>
      <text x="33" y="114" font-size="9.5" font-weight="700" text-anchor="middle" fill="var(--ink)">Silver</text>
      <rect x="58" y="102" width="46" height="16" fill="none" stroke="#333" stroke-width=".5"/>
      <line x1="58" y1="110" x2="104" y2="110" stroke="#333" stroke-width=".5"/>
      <text x="81" y="108.5" font-size="6" text-anchor="middle" fill="var(--ink)">25 Pack</text>
      <text x="81" y="116.5" font-size="5" text-anchor="middle" fill="var(--ink)">120gsm</text>
    </svg>
  </section>

  <!-- FRONT: C6 envelopes -->
  <section class="sheet sheet--c6" aria-label="C6 metallic envelopes, front">
    <svg class="front-label front-label--env" viewBox="0 0 112 122">
      <rect width="112" height="122" fill="var(--paper)"/>
      <path d="M0 0H112V9C75 11 30 16 0 24Z" fill="var(--band)"/>
      <path d="M0 25C30 17 75 11 112 10" fill="none" stroke="var(--gold)" stroke-width="1.7"/>
      <circle cx="6" cy="10" r="2.5" fill="var(--brand)"/>
      <text x="11" y="13" font-size="7.5" fill="var(--brand)">Vel Moro</text>
      <text x="109" y="38" font-size="13" text-anchor="end" fill="var(--ink)">Premium</text>
      <text x="109" y="48" font-size="9" text-anchor="end" fill="var(--ink-soft)">Metallic Card</text>
      <circle cx="21" cy="72" r="8" fill="none" stroke="var(--ink)" stroke-width="1.3"/>
      <text x="75" y="88" font-size="30" text-anchor="middle" fill="var(--ink)">C6</text>
      <text x="75" y="96" font-size="6" text-anchor="middle" fill="var(--ink)">ENVELOPES</text>
      <rect x="10" y="102" width="46" height="17" fill="var(--tab)" stroke="#555" stroke-width=".5"/>
      <text x="33" y="114" font-size="9.5" font-weight="700" text-anchor="middle" fill="var(--ink)">Silver</text>
      <rect x="58" y="102" width="46" height="16" fill="none" stroke="#333" stroke-width=".5"/>
      <line x1="58" y1="110" x2="104" y2="110" stroke="#333" stroke-width=".5"/>
      <text x="81" y="108.5" font-size="6" text-anchor="middle" fill="var(--ink)">25 Pack</text>
      <text x="81" y="116.5" font-size="5" text-anchor="middle" fill="var(--ink)">120gsm</text>
    </svg>
  </section>

  <!-- BACKS -->
  <section class="sheet sheet--a4-light-back" aria-label="A4 metallic card, back">
    <div class="back-label">
      <div class="back-label__top">
        <svg viewBox="0 0 144 65" preserveAspectRatio="none"><path d="M0 0H144V12C90 16 35 36 0 62Z" fill="var(--band)"/><path d="M0 64C35 38 90 18 144 14" fill="none" stroke="var(--gold)" stroke-width="2"/></svg>
        <span class="brand"><span class="brand__dot"></span>Vel Moro</span>
      </div>
      <div class="back-label__title"><span class="product">Premium</span><span class="finish">Metallic Card</span></div>
      <ul class="uses"><li>Ideal for office use</li><li>Ideal for card making for all occasions</li><li>Invitations for all Celebrations</li><li>Creative card &amp; paper for presentations</li><li>Acid free</li></ul>
      <div class="gallery">
        <div class="gallery__tile" role="img" aria-label="Photo of a handmade card" style="background:#eadbdc"></div>
        <div class="gallery__tile" role="img" aria-label="Photo of a handmade card" style="background:#8a5a44"></div>
        <div class="gallery__tile" role="img" aria-label="Photo of a handmade card" style="background:#9a8a5c"></div>
        <div class="gallery__tile" role="img" aria-label="Photo of a handmade card" style="background:#3d4a5c"></div>
        <div class="gallery__tile" role="img" aria-label="Photo of a handmade card" style="background:#b07a86"></div>
        <div class="gallery__tile" role="img" aria-label="Photo of a handmade card" style="background:#7e6a6a"></div>
        <div class="gallery__tile" role="img" aria-label="Photo of a handmade card" style="background:#5a5a5a"></div>
        <div class="gallery__tile" role="img" aria-label="Photo of a handmade card" style="background:#b8b4b0"></div>
        <div class="gallery__tile" role="img" aria-label="Photo of a handmade card" style="background:#a8403e"></div>
        <div class="gallery__tile" role="img" aria-label="Photo of a handmade card" style="background:#6f7c6a"></div>
        <div class="gallery__tile" role="img" aria-label="Photo of a handmade card" style="background:#d79aac"></div>
        <div class="gallery__tile" role="img" aria-label="Photo of a handmade card" style="background:#a9a1a3"></div>
      </div>
      <p class="more-info">Look for more suggestions on our information sheet or visit our website: <a href="#">www.velmoro.example</a></p>
      <div class="range">Also available in the Vel Moro Range:<ul><li>A4 Paper</li><li>A4 Vellum</li><li>90 x 110 Card</li><li>C6 Envelopes</li><li>DL Envelopes</li><li>150 x 150 Envelopes</li><li>Invitation Kits</li></ul></div>
      <div class="back-label__bottom">
        <svg viewBox="0 0 144 60" preserveAspectRatio="none"><path d="M0 60V40C40 30 100 18 144 6V60Z" fill="var(--band)"/><path d="M0 38C40 28 100 16 144 4" fill="none" stroke="var(--gold-light)" stroke-width="1.6"/></svg>
        <span class="origin">Made in China</span>
      </div>
    </div>
  </section>

  <section class="sheet sheet--a4-heavy-back" aria-label="A4 metallic card 260gsm, back">
    <div class="back-label">
      <div class="back-label__top">
        <svg viewBox="0 0 144 65" preserveAspectRatio="none"><path d="M0 0H144V12C90 16 35 36 0 62Z" fill="var(--band)"/><path d="M0 64C35 38 90 18 144 14" fill="none" stroke="var(--gold)" stroke-width="2"/></svg>
        <span class="brand"><span class="brand__dot"></span>Vel Moro</span>
      </div>
      <div class="back-label__title"><span class="product">Premium</span><span class="finish">Metallic Card</span></div>
      <ul class="uses"><li>Ideal for office use</li><li>Ideal for card making for all occasions</li><li>Invitations for all Celebrations</li><li>Creative card &amp; paper for presentations</li><li>Acid free</li></ul>
      <div class="gallery">
        <div class="gallery__tile" role="img" aria-label="Photo of a handmade card" style="background:#eadbdc"></div>
        <div class="gallery__tile" role="img" aria-label="Photo of a handmade card" style="background:#8a5a44"></div>
        <div class="gallery__tile" role="img" aria-label="Photo of a handmade card" style="background:#9a8a5c"></div>
        <div class="gallery__tile" role="img" aria-label="Photo of a handmade card" style="background:#3d4a5c"></div>
        <div class="gallery__tile" role="img" aria-label="Photo of a handmade card" style="background:#b07a86"></div>
        <div class="gallery__tile" role="img" aria-label="Photo of a handmade card" style="background:#7e6a6a"></div>
        <div class="gallery__tile" role="img" aria-label="Photo of a handmade card" style="background:#5a5a5a"></div>
        <div class="gallery__tile" role="img" aria-label="Photo of a handmade card" style="background:#b8b4b0"></div>
        <div class="gallery__tile" role="img" aria-label="Photo of a handmade card" style="background:#a8403e"></div>
        <div class="gallery__tile" role="img" aria-label="Photo of a handmade card" style="background:#6f7c6a"></div>
        <div class="gallery__tile" role="img" aria-label="Photo of a handmade card" style="background:#d79aac"></div>
        <div class="gallery__tile" role="img" aria-label="Photo of a handmade card" style="background:#a9a1a3"></div>
      </div>
      <p class="more-info">Look for more suggestions on our information sheet or visit our website: <a href="#">www.velmoro.example</a></p>
      <div class="range">Also available in the Vel Moro Range:<ul><li>A4 Paper</li><li>A4 Vellum</li><li>90 x 110 Card</li><li>C6 Envelopes</li><li>DL Envelopes</li><li>150 x 150 Envelopes</li><li>Invitation Kits</li></ul></div>
      <div class="back-label__bottom">
        <svg viewBox="0 0 144 60" preserveAspectRatio="none"><path d="M0 60V40C40 30 100 18 144 6V60Z" fill="var(--band)"/><path d="M0 38C40 28 100 16 144 4" fill="none" stroke="var(--gold-light)" stroke-width="1.6"/></svg>
        <span class="origin">Made in China</span>
      </div>
    </div>
  </section>

  <section class="sheet sheet--dl-back" aria-label="DL metallic envelopes, back">
    <div class="back-label back-label--dl">
      <div class="back-label__top">
        <svg viewBox="0 0 144 65" preserveAspectRatio="none"><path d="M0 0H144V12C90 16 35 36 0 62Z" fill="var(--band)"/><path d="M0 64C35 38 90 18 144 14" fill="none" stroke="var(--gold)" stroke-width="2"/></svg>
        <span class="brand"><span class="brand__dot"></span>Vel Moro</span>
      </div>
      <div class="back-label__title"><span class="product">Premium</span><span class="finish">Metallic Card</span></div>
      <ul class="uses"><li>Ideal for office use</li><li>Ideal for card making for all occasions</li><li>Invitations for all Celebrations</li><li>Creative card &amp; paper for presentations</li><li>Acid free</li></ul>
      <div class="gallery">
        <div class="gallery__tile" role="img" aria-label="Photo of a handmade card" style="background:#eadbdc"></div>
        <div class="gallery__tile" role="img" aria-label="Photo of a handmade card" style="background:#8a5a44"></div>
        <div class="gallery__tile" role="img" aria-label="Photo of a handmade card" style="background:#9a8a5c"></div>
        <div class="gallery__tile" role="img" aria-label="Photo of a handmade card" style="background:#3d4a5c"></div>
        <div class="gallery__tile" role="img" aria-label="Photo of a handmade card" style="background:#b07a86"></div>
        <div class="gallery__tile" role="img" aria-label="Photo of a handmade card" style="background:#7e6a6a"></div>
        <div class="gallery__tile" role="img" aria-label="Photo of a handmade card" style="background:#5a5a5a"></div>
        <div class="gallery__tile" role="img" aria-label="Photo of a handmade card" style="background:#b8b4b0"></div>
        <div class="gallery__tile" role="img" aria-label="Photo of a handmade card" style="background:#a8403e"></div>
        <div class="gallery__tile" role="img" aria-label="Photo of a handmade card" style="background:#6f7c6a"></div>
        <div class="gallery__tile" role="img" aria-label="Photo of a handmade card" style="background:#d79aac"></div>
        <div class="gallery__tile" role="img" aria-label="Photo of a handmade card" style="background:#a9a1a3"></div>
      </div>
      <p class="more-info">Look for more suggestions on our information sheet or visit our website: <a href="#">www.velmoro.example</a></p>
      <div class="range">Also available in the Vel Moro Range:<ul><li>A4 Paper</li><li>A4 Vellum</li><li>90 x 110 Card</li><li>C6 Envelopes</li><li>DL Envelopes</li><li>150 x 150 Envelopes</li><li>Invitation Kits</li></ul></div>
      <div class="back-label__bottom">
        <svg viewBox="0 0 144 60" preserveAspectRatio="none"><path d="M0 60V40C40 30 100 18 144 6V60Z" fill="var(--band)"/><path d="M0 38C40 28 100 16 144 4" fill="none" stroke="var(--gold-light)" stroke-width="1.6"/></svg>
        <span class="origin">Made in China</span>
      </div>
    </div>
  </section>

  <section class="sheet sheet--c6-back" aria-label="C6 metallic envelopes, back">
    <div class="back-label back-label--c6">
      <div class="back-label__top">
        <svg viewBox="0 0 144 65" preserveAspectRatio="none"><path d="M0 0H144V12C90 16 35 36 0 62Z" fill="var(--band)"/><path d="M0 64C35 38 90 18 144 14" fill="none" stroke="var(--gold)" stroke-width="2"/></svg>
        <span class="brand"><span class="brand__dot"></span>Vel Moro</span>
      </div>
      <div class="back-label__title"><span class="product">Premium</span><span class="finish">Metallic Card</span></div>
      <ul class="uses"><li>Ideal for office use</li><li>Ideal for card making for all occasions</li><li>Invitations for all Celebrations</li><li>Creative card &amp; paper for presentations</li><li>Acid free</li></ul>
      <div class="gallery">
        <div class="gallery__tile" role="img" aria-label="Photo of a handmade card" style="background:#eadbdc"></div>
        <div class="gallery__tile" role="img" aria-label="Photo of a handmade card" style="background:#8a5a44"></div>
        <div class="gallery__tile" role="img" aria-label="Photo of a handmade card" style="background:#9a8a5c"></div>
        <div class="gallery__tile" role="img" aria-label="Photo of a handmade card" style="background:#3d4a5c"></div>
        <div class="gallery__tile" role="img" aria-label="Photo of a handmade card" style="background:#b07a86"></div>
        <div class="gallery__tile" role="img" aria-label="Photo of a handmade card" style="background:#7e6a6a"></div>
        <div class="gallery__tile" role="img" aria-label="Photo of a handmade card" style="background:#5a5a5a"></div>
        <div class="gallery__tile" role="img" aria-label="Photo of a handmade card" style="background:#b8b4b0"></div>
        <div class="gallery__tile" role="img" aria-label="Photo of a handmade card" style="background:#a8403e"></div>
        <div class="gallery__tile" role="img" aria-label="Photo of a handmade card" style="background:#6f7c6a"></div>
        <div class="gallery__tile" role="img" aria-label="Photo of a handmade card" style="background:#d79aac"></div>
        <div class="gallery__tile" role="img" aria-label="Photo of a handmade card" style="background:#a9a1a3"></div>
      </div>
      <p class="more-info">Look for more suggestions on our information sheet or visit our website: <a href="#">www.velmoro.example</a></p>
      <div class="range">Also available in the Vel Moro Range:<ul><li>A4 Paper</li><li>A4 Vellum</li><li>90 x 110 Card</li><li>C6 Envelopes</li><li>DL Envelopes</li><li>150 x 150 Envelopes</li><li>Invitation Kits</li></ul></div>
      <div class="back-label__bottom">
        <svg viewBox="0 0 144 60" preserveAspectRatio="none"><path d="M0 60V40C40 30 100 18 144 6V60Z" fill="var(--band)"/><path d="M0 38C40 28 100 16 144 4" fill="none" stroke="var(--gold-light)" stroke-width="1.6"/></svg>
        <span class="origin">Made in China</span>
      </div>
    </div>
  </section>

</main>
</body>
</html>
```